Probate (Legal) Wordpress Design with Coding for Online Company

I need a Wordpress design with coding, pictures, content to be provided by me, fully responsive, and development. This is for a 6-7 page design.

Pages Needed: Home/About/Probate/Process/FAQ/Contact Us/Blog.

The home page should be organized as followed:
-Steps in Probate: Gather; Implement; Close (each step will come with content)
-Flat-Fee Price & Savings: Content will go here with a button to contact us (phone number) or just the phone number.
-You Have Questions, We Have Answers: five questions with content. Only one question answer to show at a time when clicked on the question from the list.
-Get to Know Us: a brief description with content about what we do and who we are.

Main image slogan: Helping Californians deal with loss with DIGNITY & UNDERSTATING (you may use a better slogan if you wish).

The Contact page should not have a map since we are an online company. We service the entire state of California in every county and city.

The About page should be simple, direct, and easy on the eye. It should have a brief description of who we are and it should have no more than 6 reasons why the client should hire us.

About our online California company. We are not attorneys but legal document assistants who prepare legal documents for probate estate when someone dies with or without a will and assets need to be distributed. We have a flat-fee for Formal Probate of $999 and $699 for Informal Probate. We are an online company and offer our services to the entire state of California in every county. We do everything over the phone and email. The turn around time for us to prepare the initial legal paperwork for the client is within 3-5 business days. We can prepare, file, serve and manage a probate matter from petition to closing. We are not attorneys so our prices are very affordable compare to the attorney.

The company name for the website will be www.thelarkwellgroup.com, The Larkwell Group.

I do not have a logo yet. The colors of the website should be easy on the eye and calming. THE SITE SHOULD BE SIMPLE AND STRAIGHT TO THE POINT. EASY TO NAVIGATE.

The company phone number should be very visible and should stand out to the client. It should also be clickable and ready to dial for smartphone users.

I do not want a contact form on the homepage. THE MAIN THING IS FOR THE POTENTIAL CLIENT TO CALL OUR OFFICE TO SIGN UP.

I do like some images of family or people since we are dealing with people who just lost a loved one. Not all the images have to be of people.

The site should not look like we practice law or that people can mistake us for attorneys.

Target Market(s)

People who just lost a loved one who had property, assets, in California but died with or without a will or trust. This is for people looking to hire non-attorneys.

Coding

Font styles to use
Serif

Colors

Designer to choose colors to be used in the design.

Requirements
Must have
• Refer to Project Description.
Nice to have
• The sample images provided is what I am attracted to for the homepage image.
Should not have

```html
<!DOCTYPE html>
<html lang="en">
<head>
<meta charset="utf-8">
<title>The Larkwell Group — Probate Document Assistance</title>
<link rel="stylesheet" href="https://fonts.googleapis.com/css2?family=Open+Sans:ital,wdth,wght@0,75..100,300..800;1,75..100,300..800&display=swap">
<style>
:root{
  --gold:#c99a1e;
  --gold-soft:#c9a35a;
  --red:#e8513a;
  --ink:#222222;
  --body:#555555;
  --line:#e6e6e6;
  --paper:#ffffff;
  --mist:#f6f6f6;
  --night:#2a2a2a;
}
*{margin:0;padding:0;box-sizing:border-box}
html,body{width:1200px;height:3429px;overflow:hidden;background:var(--paper)}
body{font-family:"Open Sans",Arial,sans-serif;color:var(--body);position:relative}
.section{position:absolute;left:0;width:1200px}
.sec-title{position:absolute;left:0;width:1200px;text-align:center;font-stretch:75%;font-weight:700;font-size:34px;color:var(--ink);letter-spacing:.5px}

/* header */
.site-header{top:0;height:155px;background:var(--paper)}
.brand{position:absolute;left:98px;top:12px;display:flex;flex-direction:column;align-items:flex-start}
.brand-dot{width:82px;height:82px;border-radius:50%;background:var(--gold);margin-left:10px}
.brand-name{margin-top:8px;font-weight:700;font-size:15px;color:#333;letter-spacing:.3px}
.call{position:absolute;right:98px;top:24px;font-size:14px;color:#777;display:flex;align-items:center;gap:6px}
.call strong{font-size:21px;color:#333;font-weight:600}
.nav{position:absolute;right:98px;top:90px;display:flex;gap:34px;font-size:13px;color:#333;align-items:center}
.nav .active{color:var(--gold);font-weight:600}
.nav .search{width:28px;height:28px;border:1px solid #ccc;border-radius:50%}

/* hero */
.hero{top:155px;height:640px;background:linear-gradient(180deg,#5d6a52 0%,#7a8a5c 40%,#a89a5a 75%,#c8b774 100%)}
.hero-line1{position:absolute;top:182px;width:1200px;text-align:center;font-stretch:75%;font-weight:300;font-size:42px;color:#fff}
.hero-line2{position:absolute;top:236px;width:1200px;text-align:center;font-weight:800;font-size:64px;color:#fff;letter-spacing:2px}
.hero-dots{position:absolute;top:550px;left:0;width:1200px;display:flex;justify-content:center;gap:6px}
.hero-dots span{width:16px;height:16px;border-radius:50%;background:#fff;opacity:.85}
.hero-dots span:first-child{background:transparent;border:2px solid #fff}
.hero-curve{position:absolute;left:0;bottom:0}

/* steps */
.steps{top:795px;height:416px}
.steps .sec-title{top:30px}
.step{position:absolute;top:138px;width:320px;height:205px;border:1px solid var(--line);text-align:center;padding:16px 26px 0}
.step svg{display:block;margin:0 auto}
.step h3{margin-top:10px;font-stretch:75%;font-weight:700;font-size:20px;color:var(--ink)}
.step p{margin-top:6px;font-size:11px;line-height:16px;color:#777}

/* flat fee */
.flatfee{top:1211px;height:476px;background:linear-gradient(180deg,#c49d52 0%,#c8a867 55%,#b79a63 100%)}
.flatfee h2{position:absolute;top:56px;width:1200px;text-align:center;font-stretch:75%;font-weight:300;font-size:50px;color:#fff}
.flatfee p{position:absolute;left:130px;width:940px;text-align:center;font-size:13px;line-height:24px;color:#fff}
.btn{position:absolute;left:510px;top:330px;width:180px;height:50px;background:var(--red);color:#fff;font-size:16px;display:flex;align-items:center;justify-content:center;letter-spacing:.5px}

/* questions */
.faq{top:1687px;height:583px;background:var(--mist)}
.faq .sec-title{top:68px}
.faq-list{position:absolute;left:98px;top:183px;width:279px;list-style:none;font-size:12px;color:#444}
.faq-list li{height:33px;border-bottom:1px solid #ddd;display:flex;align-items:center;gap:6px;padding-left:6px}
.faq-list li.open{background:var(--gold);color:#fff;border:none;height:30px;margin-bottom:3px}
.qmark{width:13px;height:13px;border-radius:50%;background:var(--red);color:#fff;font-size:9px;font-weight:700;display:flex;align-items:center;justify-content:center}
.faq-list li.open .qmark{background:#fff;color:var(--gold)}
.faq-photo{position:absolute;left:420px;top:203px;width:284px;height:293px;background:#efe2c4;padding:14px}
.faq-photo div{width:100%;height:100%;background:linear-gradient(160deg,#6f7e92 0%,#a9b6c4 55%,#d9dee4 100%)}
.faq-answer{position:absolute;left:752px;top:210px;width:350px}
.faq-answer h4{font-size:15px;font-weight:600;color:#222}
.faq-answer p{margin-top:12px;padding-left:2px;font-size:12px;line-height:19px;color:#555}

/* get to know */
.know{top:2270px;height:397px;background:linear-gradient(120deg,#efe8e0 0%,#e4d9cd 60%,#d8cbbd 100%)}
.know-red{position:absolute;left:0;top:0}
.know .sec-title{top:50px;color:#fff}
.know h3{position:absolute;top:128px;font-weight:600;font-size:25px;letter-spacing:.5px}
.know .what{left:98px;color:#fff}
.know .who{left:680px;width:440px;text-align:center;color:#222}
.know p{position:absolute;font-size:12px;line-height:19px}
.know .what-text{left:98px;top:176px;width:448px;color:#fff}
.know .who-text{left:680px;top:176px;width:440px;text-align:center;color:#333}

/* about */
.about{top:2667px;height:430px;background:linear-gradient(180deg,#ffffff 0%,#fbf7f0 55%,#e9d3b6 85%,#d7b898 100%)}
.about .sec-title{top:88px}
.about p{position:absolute;left:185px;top:176px;width:830px;text-align:center;font-size:12.5px;line-height:25px;color:#333}

/* footer */
.footer{top:3097px;height:332px;background:var(--night);color:#ddd}
.footer h5{position:absolute;top:50px;font-size:14px;font-weight:700;color:#fff}
.footer ul{position:absolute;top:94px;list-style:none;font-size:14px;line-height:32px;color:#ddd}
.contact-row{position:absolute;left:544px;display:flex;align-items:center;gap:10px;font-size:14px}
.social{position:absolute;left:882px;top:103px;display:flex;gap:10px}
.social span{width:38px;height:38px;border-radius:50%;background:#fff}
.foot-rule{position:absolute;left:98px;top:258px;width:1004px;height:1px;background:#555}
.copy{position:absolute;left:98px;top:285px;font-size:12px;color:#ccc}
</style>
</head>
<body>

<header class="section site-header">
  <div class="brand"><span class="brand-dot"></span><span class="brand-name">THE LARKWELL GROUP</span></div>
  <div class="call">
    <svg width="14" height="14" viewBox="0 0 24 24"><path fill="#c99a1e" d="M6.6 10.8a15 15 0 0 0 6.6 6.6l2.2-2.2a1 1 0 0 1 1-.25 11.4 11.4 0 0 0 3.6.6 1 1 0 0 1 1 1V20a1 1 0 0 1-1 1A17 17 0 0 1 3 4a1 1 0 0 1 1-1h3.5a1 1 0 0 1 1 1c0 1.25.2 2.45.6 3.6a1 1 0 0 1-.25 1z"/></svg>
    Call Us: <strong>(001) 555-01942</strong>
  </div>
  <nav class="nav">
    <span class="active">Home</span><span>About ▾</span><span>Probate ▾</span><span>Process ▾</span><span>FAQ</span><span>Contact Us</span><span>Blog</span><span class="search"></span>
  </nav>
</header>

<section class="section hero">
  <div role="img" aria-label="Family of several generations walking hand in hand through a sunny forest meadow" style="position:absolute;inset:0"></div>
  <div class="hero-line1">Helping Californians deal with loss with</div>
  <div class="hero-line2">DIGNITY &amp; UNDERSTATING</div>
  <div class="hero-dots"><span></span><span></span><span></span><span></span></div>
  <svg class="hero-curve" width="1200" height="110" viewBox="0 0 1200 110"><path d="M0 40 Q600 140 1200 40 L1200 110 L0 110Z" fill="#fff"/></svg>
</section>

<section class="section steps">
  <h2 class="sec-title">STEPS IN PROBATE</h2>
  <div class="step" style="left:98px">
    <svg width="48" height="40" viewBox="0 0 48 40"><path d="M4 6 Q14 2 23 8 V36 Q14 30 4 34Z M25 8 Q34 2 44 6 V34 Q34 30 25 36Z" fill="#c99a1e"/></svg>
    <h3>GATHER</h3>
    <p>Lorem Ipsum has been the industry's standard dummy text ever since the 1500s, when an unknown printer took a galley of type and scrambled it to make a type specimen book</p>
  </div>
  <div class="step" style="left:439px">
    <svg width="48" height="48" viewBox="0 0 48 48"><path d="M10 40 L14 30 L36 8 L42 14 L20 36Z" fill="none" stroke="#c99a1e" stroke-width="4" stroke-linejoin="round"/><path d="M10 40 L14 30 L20 36Z" fill="#c99a1e"/></svg>
    <h3>IMPLEMENT</h3>
    <p>Lorem Ipsum has been the industry's standard dummy text ever since the 1500s, when an unknown printer took a galley of type and scrambled it to make a type specimen book</p>
  </div>
  <div class="step" style="left:779px">
    <svg width="48" height="48" viewBox="0 0 48 48"><path d="M10 8 L40 40 M40 8 L10 40" stroke="#c99a1e" stroke-width="8"/></svg>
    <h3>CLOSE</h3>
    <p>Lorem Ipsum has been the industry's standard dummy text ever since the 1500s, when an unknown printer took a galley of type and scrambled it to make a type specimen book</p>
  </div>
</section>

<section class="section flatfee" role="img" aria-label="Warm golden tint over a city skyline at sunset">
  <h2>FLAT-FEE PRICE &amp; SAVINGS</h2>
  <p style="top:140px">Contrary to popular belief, Lorem Ipsum is not simply random text. It has roots in a piece of classical Latin literature from 45 BC, making it over 2000 years old. Edwin Marlowe, a Latin professor at Ashgrove College in Vermont, looked up one of the more obscure Latin words, consectetur, from a Lorem Ipsum passage, and going through the cites of the word in classical literature, discovered the undoubtable source.</p>
  <p style="top:230px">There are many variations of passages of Lorem Ipsum available, but the majority have suffered alteration in some form, by injected humour, or randomised words which don't look even slightly believable.</p>
  <div class="btn">CONTACT US</div>
</section>

<section class="section faq">
  <h2 class="sec-title">YOU HAVE QUESTIONS</h2>
  <ul class="faq-list">
    <li class="open"><span class="qmark">?</span>Why do Helping Californians deal with loss ?</li>
    <li><span class="qmark">?</span>Can I just do it myself?</li>
    <li><span class="qmark">?</span>How much will it cost?</li>
    <li><span class="qmark">?</span>How long does it take?</li>
    <li><span class="qmark">?</span>How do I keep my estate plan up to date?</li>
  </ul>
  <div class="faq-photo"><div role="img" aria-label="Pen resting on documents on a desk, hands shaking in the background"></div></div>
  <div class="faq-answer">
    <h4>Why do Helping Californians deal with loss ?</h4>
    <p>But I must explain to you how all this mistaken idea of denouncing pleasure and praising pain was born and I will give you a complete account of the system, and expound the actual teachings of the great explorer of the truth, the master-builder of human happiness. No one rejects, dislikes, or avoids pleasure itself, because it is pleasure, but because those who do not know how to pursue pleasure rationally encounter consequences that are extremely painful. Nor again is there anyone who loves or pursues or desires to obtain pain of itself, because it is pain, but because occasionally circumstances occur in which toil and pain can procure him some great pleasure.</p>
  </div>
</section>

<section class="section know">
  <div role="img" aria-label="Hand signing papers on a desk, softly faded" style="position:absolute;inset:0"></div>
  <svg class="know-red" width="700" height="397" viewBox="0 0 700 397"><path d="M0 0 H686 L560 397 H0Z" fill="#e8513a"/></svg>
  <h2 class="sec-title">GET TO KNOW US</h2>
  <h3 class="what">WHAT WE DO</h3>
  <p class="what-text">At vero eos et accusamus et iusto odio dignissimos ducimus qui blanditiis praesentium voluptatum deleniti atque corrupti quos dolores et quas molestias excepturi sint occaecati cupiditate non provident, similique sunt in culpa qui officia deserunt mollitia animi, id est laborum et dolorum fuga. Et harum quidem rerum facilis est et expedita distinctio. Nam libero tempore, cum soluta nobis est eligendi optio cumque nihil impedit quo minus id quod maxime placeat facere possimus, omnis voluptas assumenda est, omnis dolor repellendus.</p>
  <h3 class="who">WHO WE ARE</h3>
  <p class="who-text">Et harum quidem rerum facilis est et expedita distinctio. Nam libero tempore, cum soluta nobis est eligendi optio cumque nihil impedit quo minus id quod maxime placeat facere possimus, omnis voluptas assumenda est, omnis dolor repellendus.<br><br>Temporibus autem quibusdam et aut officiis debitis aut rerum necessitatibus saepe eveniet ut et voluptates repudiandae sint et molestiae non recusandae.</p>
</section>

<section class="section about">
  <div role="img" aria-label="Couple walking on a beach at sunset, softly faded" style="position:absolute;inset:0"></div>
  <h2 class="sec-title">ABOUT OUR ONLINE CALIFORNIA COMPANY</h2>
  <p>We are not attorneys but legal document assistants who prepare legal documents for probate estate when someone dies with or without a will and assets need to be distributed. We have a flat-fee for Formal Probate of $999 and $699 for Informal Probate. We are an online company and offer our services to the entire state of California in every county. We do everything over the phone and email. The turn around time for us to prepare the initial legal paperwork for the client is within 3-5 business days. We can prepare, file, serve and manage a probate matter from petition to closing. We are not attorneys so our prices are very affordable compare to the attorney.</p>
</section>

<footer class="section footer">
  <h5 style="left:98px">QUICK LINKS</h5>
  <ul style="left:98px"><li>Home</li><li>About</li><li>Probate</li><li>Process</li></ul>
  <ul style="left:297px"><li>FAQ</li><li>Contact Us</li><li>Blog</li></ul>
  <h5 style="left:544px">CONTACT US</h5>
  <div class="contact-row" style="top:103px">
    <svg width="14" height="14" viewBox="0 0 24 24"><path fill="#ddd" d="M6.6 10.8a15 15 0 0 0 6.6 6.6l2.2-2.2a1 1 0 0 1 1-.25 11.4 11.4 0 0 0 3.6.6 1 1 0 0 1 1 1V20a1 1 0 0 1-1 1A17 17 0 0 1 3 4a1 1 0 0 1 1-1h3.5a1 1 0 0 1 1 1c0 1.25.2 2.45.6 3.6a1 1 0 0 1-.25 1z"/></svg>
    (001) 555-01942
  </div>
  <div class="contact-row" style="top:136px">
    <svg width="14" height="12" viewBox="0 0 24 20"><rect x="1" y="1" width="22" height="18" fill="#ddd"/><path d="M1 1 L12 11 L23 1" fill="none" stroke="#2a2a2a" stroke-width="2"/></svg>
    info@thelarkwellgroup.com
  </div>
  <h5 style="left:882px">CONNECT WITH SOCIAL MEDIA</h5>
  <div class="social" aria-label="Social media links"><span></span><span></span><span></span><span></span></div>
  <div class="foot-rule"></div>
  <div class="copy">Copyright © 2017 The Larkwell Group&nbsp; | &nbsp;All Rights Reserved&nbsp; | &nbsp;Disclaimer&nbsp; | &nbsp;Terms of Use&nbsp; | &nbsp;Privacy Policy</div>
</footer>

</body>
</html>
```